Criação de Papelaria Profissional para Limpeza & Serviço para o lar
" Nossa empresa e familiar, buscamos fazer nosso trabalho com excelencia e qualidade visando o bem estar de nossos clientes. "

```html
<!DOCTYPE html>
<html lang="en">
<head>
<meta charset="utf-8">
<title>BrightNest Cleaning LLC – Stickers</title>
<link href="https://fonts.googleapis.com/css2?family=Poppins:wght@500;600;700&display=swap" rel="stylesheet">
<style>
  :root {
    --backdrop: #b3c4be;
    --mint: #5fc2a2;
    --copper: #c8874f;
    --paper: #f7f7f5;
    --white: #ffffff;
  }
  * { margin: 0; padding: 0; box-sizing: border-box; }
  html, body { width: 1200px; height: 1200px; overflow: hidden; }
  body {
    background: var(--backdrop);
    font-family: "Poppins", sans-serif;
    position: relative;
  }
  .sticker { position: absolute; }

  .brand { display: flex; flex-direction: column; align-items: center; }
  .brand__dot {
    display: block;
    width: 58px; height: 58px; border-radius: 50%;
    background: var(--copper);
    margin-bottom: 12px;
  }
  .brand__name { font-weight: 700; line-height: 1.2; letter-spacing: -0.5px; white-space: nowrap; }
  .brand__sub { font-weight: 700; letter-spacing: 5px; line-height: 1; margin-top: 6px; white-space: nowrap; }

  /* Round sticker */
  .sticker--round {
    left: 60px; top: 300px;
    width: 432px; height: 432px;
    border-radius: 50%;
    background: var(--mint);
    display: flex; flex-direction: column; align-items: center; justify-content: center;
    padding-top: 56px;
  }
  .sticker--round .ring {
    position: absolute; inset: 20px;
    border: 4px solid var(--copper);
    border-radius: 50%;
  }
  .sticker--round .brand__name,
  .sticker--round .brand__sub { color: var(--white); }
  .sticker--round .brand__name { font-size: 42px; }
  .sticker--round .brand__sub { font-size: 13px; }
  .sticker--round .contact {
    margin-top: 24px; color: var(--white);
    font-size: 13px; font-weight: 500; line-height: 1.6; text-align: left;
    align-self: center; width: 150px; margin-left: -4px;
  }

  /* Rectangular sticker */
  .sticker--card {
    left: 554px; top: 259px;
    width: 448px; height: 442px;
    border-radius: 26px;
    background: var(--paper);
    display: flex; flex-direction: column; align-items: center; justify-content: center;
  }
  .sticker--card .brand__name,
  .sticker--card .brand__sub { color: var(--mint); }
  .sticker--card .brand__name { font-size: 54px; }
  .sticker--card .brand__sub { font-size: 16px; letter-spacing: 6px; margin-top: 8px; }
  .sticker--card .brand__dot { width: 70px; height: 70px; }
  .sticker--card .contact {
    margin-top: 36px; display: flex; gap: 60px;
    color: var(--copper); font-size: 15px; font-weight: 600;
  }

  /* Strip sticker */
  .sticker--strip {
    left: 619px; top: 750px;
    width: 440px; height: 150px;
    border-radius: 6px;
    background: var(--mint);
    display: flex; flex-direction: column; align-items: center; justify-content: center;
  }
  .strip__brand { display: flex; align-items: center; gap: 16px; }
  .sticker--strip .brand__dot { width: 52px; height: 52px; margin: 0; }
  .sticker--strip .brand { align-items: flex-end; }
  .sticker--strip .brand__name,
  .sticker--strip .brand__sub { color: var(--white); }
  .sticker--strip .brand__name { font-size: 42px; }
  .sticker--strip .brand__sub { font-size: 11px; letter-spacing: 4px; margin-top: 4px; }
  .sticker--strip .contact {
    margin-top: 12px; display: flex; gap: 50px;
    color: var(--copper); font-size: 10px; font-weight: 600;
  }
</style>
</head>
<body>
  <div class="sticker sticker--round">
    <div class="ring"></div>
    <div class="brand">
      <span class="brand__dot"></span>
      <span class="brand__name">BrightNest</span>
      <span class="brand__sub">CLEANING LLC</span>
    </div>
    <div class="contact">
      <p>(00) 99000-5186</p>
      <p>@brightnestcleaning</p>
    </div>
  </div>

  <div class="sticker sticker--card">
    <div class="brand">
      <span class="brand__dot"></span>
      <span class="brand__name">BrightNest</span>
      <span class="brand__sub">CLEANING LLC</span>
    </div>
    <div class="contact">
      <span>(00) 99000-5186</span>
      <span>@brightnestcleaning</span>
    </div>
  </div>

  <div class="sticker sticker--strip">
    <div class="strip__brand">
      <span class="brand__dot"></span>
      <div class="brand">
        <span class="brand__name">BrightNest</span>
        <span class="brand__sub">CLEANING LLC</span>
      </div>
    </div>
    <div class="contact">
      <span>(00) 99000-5186</span>
      <span>@brightnestcleaning</span>
    </div>
  </div>
</body>
</html>
```